We need a logo that works well with baseball caps, tee shirts and sweat shirts. We are a carpentry framing company specializing in apartment complexes and large residential communities. We work in what is known as the tri state area southeastern Pennsylvania , New Jersey and northern Delaware . We would like to see die signs using the old English letter M and royal blue colors. Also we stress OSHA compliance and safety.

Residential

Dalworth Construction Co Inc
4318 Briscoe Lane
Corvale NJ 08117
Glen Dalworth
glen1dalworth@postvane.example
267-581-9026

```html
<!DOCTYPE html>
<html lang="en">
<head>
<meta charset="utf-8">
<title>Dalworth Construction – Business Card</title>
<link rel="stylesheet" href="https://fonts.googleapis.com/css2?family=Jost:wght@400;500;700&display=swap">
<style>
  :root {
    --backdrop: #e4e2de;
    --card: #f7f6f2;
    --royal-navy: #1f2d6b;
    --ink-grey: #4a4a4f;
    --card-shadow: rgba(0, 0, 0, 0.18);
  }
  * { box-sizing: border-box; margin: 0; padding: 0; }
  html, body {
    width: 1200px;
    height: 800px;
    overflow: hidden;
    background: var(--backdrop);
    font-family: "Jost", "Futura", sans-serif;
  }
  .stage {
    width: 1200px;
    height: 800px;
    display: flex;
    align-items: center;
    justify-content: center;
  }
  .business-card {
    position: relative;
    width: 840px;
    height: 480px;
    background: var(--card);
    box-shadow: 0 10px 30px var(--card-shadow);
    display: flex;
  }
  .brand-panel {
    width: 330px;
    display: flex;
    flex-direction: column;
    align-items: center;
    justify-content: center;
    gap: 14px;
    padding-top: 40px;
  }
  .brand-square {
    width: 22px;
    height: 22px;
    background: var(--royal-navy);
  }
  .brand-name {
    color: var(--royal-navy);
    font-weight: 500;
    font-size: 26px;
    line-height: 1.15;
    text-align: center;
    letter-spacing: 0.02em;
  }
  .divider {
    position: absolute;
    left: 330px;
    top: 90px;
    width: 2px;
    height: 230px;
    background: var(--royal-navy);
  }
  .contact-panel {
    flex: 1;
    padding: 110px 70px 50px 40px;
    display: flex;
    flex-direction: column;
    align-items: flex-end;
    text-align: right;
  }
  .person-name {
    color: var(--royal-navy);
    font-weight: 700;
    font-size: 42px;
    line-height: 1;
    margin-bottom: 12px;
  }
  .address {
    color: var(--ink-grey);
    font-size: 16px;
    line-height: 1.2;
    margin-bottom: 12px;
    margin-right: 28px;
  }
  .contact-line {
    display: flex;
    align-items: center;
    gap: 10px;
    color: var(--ink-grey);
    font-size: 16px;
    line-height: 1.6;
  }
  .contact-line svg { width: 18px; height: 18px; }
  .safety-tagline {
    margin-top: auto;
    color: var(--royal-navy);
    font-size: 17px;
    letter-spacing: 0.02em;
  }
</style>
</head>
<body>
  <main class="stage">
    <article class="business-card">
      <section class="brand-panel">
        <span class="brand-square" aria-hidden="true"></span>
        <p class="brand-name">Dalworth<br>Construction</p>
      </section>

      <span class="divider" aria-hidden="true"></span>

      <section class="contact-panel">
        <h1 class="person-name">Glen Dalworth</h1>
        <p class="address">4318 Briscoe Lane<br>Corvale NJ 08117</p>
        <p class="contact-line">
          glen1dalworth@postvane.example
          <svg viewBox="0 0 18 18" aria-label="Email" role="img">
            <rect x="1.5" y="4" width="15" height="10" fill="none" stroke="#4a4a4f" stroke-width="1.4"/>
            <path d="M1.5 4 L9 10 L16.5 4" fill="none" stroke="#4a4a4f" stroke-width="1.4"/>
          </svg>
        </p>
        <p class="contact-line">
          267-581-9026
          <svg viewBox="0 0 18 18" aria-label="Mobile phone" role="img">
            <rect x="5" y="1.5" width="8" height="15" rx="1.5" fill="none" stroke="#4a4a4f" stroke-width="1.4"/>
            <line x1="8" y1="14" x2="10" y2="14" stroke="#4a4a4f" stroke-width="1.4"/>
          </svg>
        </p>
        <p class="safety-tagline">OSHA compliance and SAFETY 1st</p>
      </section>
    </article>
  </main>
</body>
</html>
```